Marigold Premium Business Card Design Project

About the company: Here at Fernhaven Botanics, we focus on cosmetic products that based on essential oils and different kinds of plant essences. All of our raw materials are pure organic and specially selected from local producers in Australia.

I'm here to look for a unique business card design, to replace the current one later on, so I don't have many requirements. Why I wanna restrict designers' creativity?

All I know is: 1. do not make it too complicated, straight forward, simple and pure. 2. this design may be used for other purposes (i.e. logo and slogan on the front, Brand Story and contact details at the back). Therefor, I'd like to have the design for 3 layouts, one only have logo, slogan, contact detials, one for the brand story, the other one for the personal business card with staff's mob etc...

A vector graphic is required, i.e. eps, ai, easy for me to resize.

Round Corner.

Thanks

Plz add "Hand made in Australia" in the design, cheers.

Target Market(s)

Women aged yr 20-50

Industry/Entity Type

Business

Requirements
Must have
• Logo: please see attacment (eps, ai)

Slogan: Moonlit Velvet Glow

Website:www.fernhavenbotanics.com.au

Address: temporary not available

Phone: temporary not available

"Hand made in Australia"

Nice to have
• Prefer round corner

```html
<!DOCTYPE html>
<html lang="en">
<head>
<meta charset="utf-8">
<title>Fernhaven Botanics – Business Card</title>
<link rel="stylesheet" href="https://fonts.googleapis.com/css2?family=Dancing+Script:wght@600&family=Questrial&display=swap">
<style>
  :root {
    --backdrop: #ece8e4;
    --card-top: #f4f2f1;
    --card-bottom: #e6e3e2;
    --card-edge: #d9d4d2;
    --band: #e7b4b6;
    --brand-red: #c8283f;
    --rose-dot: #d94a63;
    --ink: #2e2b2c;
    --ink-soft: #4a4546;
  }
  * { margin: 0; padding: 0; box-sizing: border-box; }
  html, body {
    width: 1200px;
    height: 970px;
    overflow: hidden;
    background: var(--backdrop);
  }
  .canvas {
    position: relative;
    width: 1200px;
    height: 970px;
  }
  .card {
    position: absolute;
    left: 100px;
    top: 205px;
    width: 1000px;
    height: 560px;
    border-radius: 40px;
    background: linear-gradient(180deg, var(--card-top), var(--card-bottom));
    border: 1px solid var(--card-edge);
    box-shadow: 0 18px 40px rgba(60, 40, 40, 0.12);
    overflow: hidden;
  }
  .brand {
    position: absolute;
    top: 48px;
    left: 0;
    width: 100%;
    display: flex;
    justify-content: center;
    align-items: center;
    gap: 22px;
  }
  .brand-dot {
    width: 58px;
    height: 58px;
    border-radius: 50%;
    background: var(--rose-dot);
  }
  .brand-name {
    font-family: "Dancing Script", cursive;
    font-weight: 600;
    font-size: 76px;
    line-height: 1.1;
    color: var(--brand-red);
  }
  .slogan {
    position: absolute;
    top: 200px;
    left: 530px;
    font-family: "Dancing Script", cursive;
    font-weight: 600;
    font-size: 30px;
    color: var(--brand-red);
  }
  .contact-band {
    position: absolute;
    top: 285px;
    left: 0;
    width: 100%;
    height: 168px;
    background: var(--band);
  }
  .contact-list {
    position: absolute;
    top: 36px;
    left: 34px;
    list-style: none;
    font-family: "Questrial", sans-serif;
    font-size: 27px;
    color: var(--ink);
  }
  .contact-list li {
    display: flex;
    align-items: center;
    gap: 14px;
    height: 34px;
  }
  .contact-list svg {
    width: 16px;
    height: 16px;
    fill: var(--ink-soft);
    flex: none;
  }
  .contact-web {
    color: var(--brand-red);
    font-weight: bold;
  }
  .address {
    position: absolute;
    top: 36px;
    left: 620px;
    font-family: "Questrial", sans-serif;
    font-size: 27px;
    line-height: 34px;
    color: var(--ink);
    font-style: normal;
  }
  .origin {
    position: absolute;
    top: 485px;
    left: 0;
    width: 100%;
    text-align: center;
    font-family: "Dancing Script", cursive;
    font-weight: 600;
    font-size: 46px;
    color: var(--ink-soft);
  }
</style>
</head>
<body>
  <main class="canvas">
    <section class="card">
      <div class="brand">
        <span class="brand-dot"></span>
        <span class="brand-name">Fernhaven Botanics</span>
      </div>
      <p class="slogan">Moonlit Velvet Glow</p>

      <div class="contact-band">
        <ul class="contact-list">
          <li>
            <svg viewBox="0 0 16 16" aria-hidden="true"><path d="M4 1.5c.6 0 1 .3 1.2.8l.9 2.2c.2.5 0 1-.4 1.3l-1 .7c.7 1.5 1.8 2.6 3.3 3.3l.7-1c.3-.4.8-.6 1.3-.4l2.2.9c.5.2.8.6.8 1.2v1.7c0 .8-.7 1.4-1.5 1.3C6.3 13.1 2.9 9.7 2.5 4.5 2.4 3.7 3 3 3.8 3z"/></svg>
            <span>+441132640718</span>
          </li>
          <li>
            <svg viewBox="0 0 16 16" aria-hidden="true"><path d="M1 3.5h14v9H1z" fill="none"/><path d="M1 3.5h14L8 9z"/><path d="M1 5l7 5.4L15 5v7.5H1z"/></svg>
            <span>clara.whitby@fernmail.com</span>
          </li>
          <li>
            <svg viewBox="0 0 16 16" aria-hidden="true"><circle cx="8" cy="8" r="7"/><path d="M1 8h14M8 1c-2.5 2.5-2.5 11.5 0 14M8 1c2.5 2.5 2.5 11.5 0 14" stroke="#e7b4b6" stroke-width="1" fill="none"/></svg>
            <span class="contact-web">www.fernhavenbotanics.com.au</span>
          </li>
        </ul>
        <address class="address">Harbour Mill, Canal Street,<br>Leeds, LS9 7RT</address>
      </div>

      <p class="origin">Hand made in Australia</p>
    </section>
  </main>
</body>
</html>
```